Design a Hemp Museum + exhibition design**

I'm creating an Online Museum for Hemp which will tell the story of hemp from ancient times to now and the future
cover the medical, industrial and nutritional uses and development of hemp
the people behind it, researchers, politicians, farmers and influencerts

the museum will have a number of "wings" , each holds an exhibition around a differnet theme, for example:

Hemp in the Age of Empires: 18th and 19th Century Collections
Hemp - The History of Healing
Domestication and Early Use: Ancient Collection
From Cotton Gin to Plastics and Prohibition: Hemp's Decline

these are just a few sample ideas for exhibitions

I'm looking for an overall design for the museum home page and exhibition page which will make people curious and want to spend time,learning and browsing

Think mobile -first :)

You are requested to design

1. Home page
2. Exhibition page

Target Market(s)

Hemp aficionados, curious fans

Logo Text

The Lumen Museum

Coding

Coded - Design and coding required

Number of Pages Required

3 page

Font styles to use
Sans Serif
Decorative

Requirements
Must have
• a homepage design which prompts visitors to immediately start watching an exhibition

visitors need to understand that this is a museum , so that they dont think it's a business, a service provider or anything like that

needs to have the usual links to T&C, privacy, about us

needs to have a link to "Wander past the lantern stall"

must have a visual WOW effect
Nice to have
• animations, sounds etc
Should not have
• forms like contact us etc - not relevant

```html
<!DOCTYPE html>
<html lang="en">
<head>
<meta charset="utf-8">
<title>The Lumen Museum — Home &amp; Exhibitions</title>
<link href="https://fonts.googleapis.com/css2?family=Playfair+Display:wght@400;700;900&family=Montserrat:wght@400;500;600&display=swap" rel="stylesheet">
<style>
:root{
  --bg-deep:#06181a;
  --bg-mid:#0c2424;
  --green:#4cc454;
  --green-btn:#4fd15a;
  --line:#2c5a45;
  --text:#ffffff;
  --text-soft:#d6dedb;
  --muted:#9fb0ab;
  --art-warm:#f6efb8;
  --frame:#e8e4cf;
}
*{margin:0;padding:0;box-sizing:border-box}
html,body{width:1200px;height:338px;overflow:hidden;background:var(--bg-deep)}
a{color:inherit;text-decoration:none}
.canvas{position:relative;width:1200px;height:338px;overflow:hidden;
  background:radial-gradient(ellipse at 70% 40%,var(--bg-mid) 0%,var(--bg-deep) 70%);
  font-family:'Montserrat',sans-serif;color:var(--text)}
.foliage{position:absolute;border-radius:50%;filter:blur(10px)}
.foliage--left{left:-50px;top:150px;width:110px;height:130px;
  background:radial-gradient(ellipse,rgba(50,105,55,.35),rgba(20,60,40,0) 70%)}
.foliage--right{right:-40px;top:-20px;width:160px;height:170px;
  background:radial-gradient(ellipse at 70% 40%,rgba(80,150,65,.4),rgba(20,60,40,0) 70%)}
.foliage--mid{left:520px;top:150px;width:200px;height:180px;
  background:radial-gradient(ellipse,rgba(30,70,50,.25),rgba(20,60,40,0) 70%)}

.brand{position:absolute;top:16px;display:flex;align-items:center;gap:4px;
  font-family:'Playfair Display',serif;font-weight:400;font-size:6.6px;color:var(--text)}
.brand__mark{width:14px;height:14px;border:1px solid #c9d3cf;border-radius:50%}

.stall-link{position:absolute;top:15px;width:63px;height:19px;background:var(--green-btn);
  color:var(--text);font-size:4.6px;font-weight:600;letter-spacing:.4px;
  display:flex;align-items:center;justify-content:center}
.stall-link::before{content:"";position:absolute;left:-3px;top:-3px;width:63px;height:19px;
  border:1px solid var(--green);border-right:none;border-bottom:none}

.title{position:absolute;top:48px;font-family:'Playfair Display',serif;font-weight:900;
  font-size:19.5px;white-space:nowrap;transform:translateX(-50%);letter-spacing:.2px;color:var(--text)}
.title em{font-style:normal;color:var(--green)}
.lede{position:absolute;top:81px;font-size:6px;color:var(--text-soft);
  transform:translateX(-50%);white-space:nowrap}

.timeline{position:absolute;left:45px;top:130px;width:1127px;height:1px;background:var(--line)}
.timeline::before,.timeline::after{content:"";position:absolute;top:-1.5px;width:4px;height:4px;
  border-radius:50%;background:var(--green)}
.timeline::before{left:-2px}.timeline::after{right:-2px}

.stop{position:absolute;top:0;width:130px;transform:translateX(-50%);text-align:center}
.stop__label{position:absolute;top:116px;left:0;right:0;font-size:6px;font-weight:600;color:var(--green)}
.stop__stem{position:absolute;left:50%;top:126px;width:1px;background:var(--line)}
.stop__art{position:absolute;left:4.5px;width:121px;height:80px;border:1.5px solid var(--frame)}
.art--painting{background:radial-gradient(ellipse at 50% 45%,#6a8a42 0%,#8ab552 30%,var(--art-warm) 62%)}
.art--sculpture{background:linear-gradient(160deg,#e9dcc0 0%,#c9c98a 40%,#7f9a4a 70%,#d9c35a 100%)}
.stop__caption{position:absolute;left:0;right:0;font-size:5.5px;line-height:10px;color:var(--text-soft)}
.stop--painting .stop__stem{height:17px}
.stop--painting .stop__art{top:152px}
.stop--painting .stop__caption{top:241px}
.stop--sculpture .stop__stem{height:42px}
.stop--sculpture .stop__art{top:176.5px}
.stop--sculpture .stop__caption{top:265.5px}

.social{position:absolute;top:324px;display:flex;gap:13px}
.social span{width:4px;height:4px;border-radius:50%;background:var(--text)}
.legal{position:absolute;top:323px;display:flex;gap:7px;font-size:4.6px;color:var(--muted)}
.legal a:hover{color:var(--green)}
.pager{position:absolute;top:322px;width:145px;height:6px}
.pager span{position:absolute;top:1.7px;width:2.6px;height:2.6px;border-radius:50%;background:var(--text)}
.pager span.is-active{top:0;width:6px;height:6px;background:transparent;border:1px solid var(--text)}
.pager span.is-active::after{content:"";position:absolute;left:1px;top:1px;width:2px;height:2px;border-radius:50%;background:var(--text)}
.count{position:absolute;top:320px;font-size:5.4px;color:var(--text)}
.count small{color:var(--muted);font-size:5.4px}
</style>
</head>
<body>
<main class="canvas">
  <div class="foliage foliage--left" role="img" aria-label="Dark green hemp leaves in the background"></div>
  <div class="foliage foliage--mid" role="img" aria-label="Faint hemp leaves in the background"></div>
  <div class="foliage foliage--right" role="img" aria-label="Bright green hemp leaves at the corner"></div>

  <!-- home page -->
  <section class="screen screen--home" aria-label="Home">
    <a class="brand" href="#home" style="left:43px"><span class="brand__mark"></span>The Lumen Museum</a>
    <a class="stall-link" href="#lantern-stall" title="Wander past the lantern stall" style="left:495px">LANTERN STALL</a>
    <h1 class="title" style="left:298px"><em>The Exhibition</em> of Lumen Museum</h1>
    <p class="lede" style="left:299px">Lorem ipsum dolor sit amet, consetetur sadipscing elitr, sed diam nonumy eirmod</p>
  </section>

  <!-- exhibition page -->
  <section class="screen screen--exhibition" aria-label="Exhibition">
    <a class="brand" href="#home" style="left:642px"><span class="brand__mark"></span>The Lumen Museum</a>
    <a class="stall-link" href="#lantern-stall" title="Wander past the lantern stall" style="left:1094px">LANTERN STALL</a>
    <h2 class="title" style="left:900px"><em>Hemp In</em>&nbsp; The Age Of Empires:</h2>
    <p class="lede" style="left:899px">Lorem ipsum dolor sit amet, consetetur sadipscing elitr, sed diam nonumy eirmod</p>
  </section>

  <div class="timeline"></div>

  <div class="stop stop--painting" style="left:136.5px"><span class="stop__label">Painting</span><span class="stop__stem"></span><div class="stop__art art--painting" role="img" aria-label="Painting of hemp leaves on a pale yellow ground"></div><p class="stop__caption">Greek anchors aweigh: powered by<br>Papyrus and Hemp</p></div>
  <div class="stop stop--sculpture" style="left:296px"><span class="stop__label">Scupture</span><span class="stop__stem"></span><div class="stop__art art--sculpture" role="img" aria-label="Botanical study of flowering plants"></div><p class="stop__caption">Greek anchors aweigh: powered by<br>Papyrus and Hemp</p></div>
  <div class="stop stop--painting" style="left:455.5px"><span class="stop__label">Painting</span><span class="stop__stem"></span><div class="stop__art art--painting" role="img" aria-label="Painting of hemp leaves on a pale yellow ground"></div><p class="stop__caption">Greek anchors aweigh: powered by<br>Papyrus and Hemp</p></div>
  <div class="stop stop--sculpture" style="left:615px"><span class="stop__label">Scupture</span><span class="stop__stem"></span><div class="stop__art art--sculpture" role="img" aria-label="Botanical study of flowering plants"></div><p class="stop__caption">Greek anchors aweigh: powered by<br>Papyrus and Hemp</p></div>
  <div class="stop stop--painting" style="left:774.5px"><span class="stop__label">Painting</span><span class="stop__stem"></span><div class="stop__art art--painting" role="img" aria-label="Painting of hemp leaves on a pale yellow ground"></div><p class="stop__caption">Greek anchors aweigh: powered by<br>Papyrus and Hemp</p></div>
  <div class="stop stop--sculpture" style="left:934px"><span class="stop__label">Scupture</span><span class="stop__stem"></span><div class="stop__art art--sculpture" role="img" aria-label="Botanical study of flowering plants"></div><p class="stop__caption">Greek anchors aweigh: powered by<br>Papyrus and Hemp</p></div>
  <div class="stop stop--painting" style="left:1093px"><span class="stop__label">Painting</span><span class="stop__stem"></span><div class="stop__art art--painting" role="img" aria-label="Painting of hemp leaves on a pale yellow ground"></div><p class="stop__caption">Greek anchors aweigh: powered by<br>Papyrus and Hemp</p></div>

  <!-- footers -->
  <footer>
    <div class="social" style="left:43px" aria-label="Social links"><span></span><span></span><span></span></div>
    <nav class="legal" style="left:100px" aria-label="Museum links"><a href="#about">About us</a><a href="#terms">T&amp;C</a><a href="#privacy">Privacy</a></nav>
    <div class="pager" style="left:229px"><span class="is-active" style="left:0"></span><span style="left:47.5px"></span><span style="left:93.5px"></span><span style="left:140px"></span></div>
    <p class="count" style="left:541px">01 / <small>04</small></p>

    <div class="social" style="left:642px" aria-label="Social links"><span></span><span></span><span></span></div>
    <nav class="legal" style="left:699px" aria-label="Museum links"><a href="#about">About us</a><a href="#terms">T&amp;C</a><a href="#privacy">Privacy</a></nav>
    <div class="pager" style="left:829px"><span style="left:1.5px"></span><span class="is-active" style="left:45.5px"></span><span style="left:93px"></span><span style="left:139.5px"></span></div>
    <p class="count" style="left:1139px">02 / <small>04</small></p>
  </footer>
</main>
</body>
</html>
```